"Broadcast Tinkerings" - podcast cover artwrok

I need podcast cover artwork for "Broadcast Tinkerings". As the name implies, it focuses on experimenting with podcasts. I started this podcast a couple years ago and am rebranding now (old name was "Lantern Workshop" with the tagline of "broadcast tinkerings).

Maybe have (in small type) "a production of Harbor Fern Audio, LLC".

I would like it to convey creativity, innovation, and simplicity.

UPDATE: I uploaded a couple other podcast artwork I like to help with inspiration.

Target Market(s)

Podcasters, bloggers, entrepreneurs

Font styles to use
Sans Serif

Colors
0355a3
acd036
faa54b

Requirements
Must have
• Colors I like are darker shades of blue, green, and tan/sand. I selected sample colors, but the shade can vary to ensure that they are complementary.
Nice to have
• I've included a cartoon image of myself that may or may not work with the design.

```html
<!DOCTYPE html>
<html lang="en">
<head>
<meta charset="utf-8">
<title>Broadcast Tinkerings – Cover Concepts</title>
<link rel="stylesheet" href="https://fonts.googleapis.com/css2?family=Montserrat:wght@600;700;800;900&display=swap">
<style>
  :root {
    --page-bg: #ece8e2;
    --night: #050505;
    --ember: #e0511c;
    --ember-soft: #ff8a3d;
    --silver: #d3d5d9;
    --royal: #0e47a1;
    --royal-deep: #0a2f78;
    --lime: #c8e02e;
    --white: #ffffff;
    --sky-top: #3f7fa6;
    --sky-mid: #e7d6d2;
    --sea: #274a6e;
    --ink: #0f1630;
    --meadow: #6f8f1f;
  }
  * { margin: 0; padding: 0; box-sizing: border-box; }
  html, body { width: 918px; height: 1200px; overflow: hidden; }
  body {
    position: relative;
    background: var(--page-bg);
    font-family: "Montserrat", sans-serif;
  }
  .cover {
    position: absolute;
    left: 277px;
    width: 364px;
    height: 364px;
    overflow: hidden;
  }
  .cover--ember { top: 26px; background: var(--night); }
  .cover--band { top: 406px; background: linear-gradient(180deg, var(--sky-top) 0%, var(--sky-mid) 40%, var(--sea) 75%); }
  .cover--meadow { top: 786px; background: linear-gradient(180deg, var(--sky-top) 0%, var(--sky-mid) 38%, var(--sea) 62%, var(--ink) 100%); }

  .host-art {
    position: absolute;
    border-radius: 48% 48% 10% 10%;
    background: linear-gradient(180deg, #2a211d 0%, #eab0a0 22%, #f4c4b6 55%, #8fd3e0 82%, #c2ebf2 100%);
  }
  .cover--ember .host-art { left: 72px; top: 22px; width: 220px; height: 222px; }
  .cover--band .host-art { left: 22px; top: 6px; width: 240px; height: 226px; }
  .cover--meadow .host-art { left: 30px; top: 22px; width: 240px; height: 236px; }

  .ember-glow { position: absolute; left: 0; top: 240px; width: 364px; height: 124px; }
  .ember-title {
    position: absolute; left: 0; top: 256px; width: 364px;
    text-align: center; color: var(--silver);
    font-size: 36px; font-weight: 800; line-height: 1.05;
  }

  .band-panel { position: absolute; left: 0; top: 232px; width: 364px; height: 132px; }
  .band-title {
    position: absolute; left: 30px; top: 256px;
    color: var(--lime); font-weight: 900; font-size: 32px; line-height: 1.05;
  }
  .band-credit {
    position: absolute; left: 230px; top: 326px;
    color: var(--lime); font-weight: 700; font-size: 7.5px; line-height: 1.35; text-align: center;
  }

  .meadow-hill { position: absolute; left: 0; top: 190px; width: 364px; height: 174px; }
  .meadow-title {
    position: absolute; left: 0; top: 272px; width: 364px; text-align: center;
    color: var(--white); font-weight: 700; font-size: 22px; line-height: 1;
  }
  .meadow-credit {
    position: absolute; left: 0; top: 322px; width: 364px; text-align: center;
    color: var(--white); font-weight: 700; font-size: 7.5px; line-height: 1.35;
  }
</style>
</head>
<body>

  <section class="cover cover--ember">
    <svg class="ember-glow" viewBox="0 0 364 124" aria-hidden="true">
      <defs>
        <radialGradient id="emberGlow" cx="0.5" cy="0.55" r="0.55">
          <stop offset="0" stop-color="#ff8a3d" stop-opacity="0.95"/>
          <stop offset="0.5" stop-color="#e0511c" stop-opacity="0.6"/>
          <stop offset="1" stop-color="#e0511c" stop-opacity="0"/>
        </radialGradient>
      </defs>
      <ellipse cx="182" cy="70" rx="200" ry="60" fill="url(#emberGlow)"/>
      <polyline points="60,10 182,115 302,10" fill="none" stroke="#e0511c" stroke-width="2" opacity="0.7"/>
    </svg>
    <div class="host-art" role="img" aria-label="Illustrated portrait of the host in a light blue shirt"></div>
    <div class="ember-title">Broadcast<br>Tinkerings</div>
  </section>

  <section class="cover cover--band">
    <div class="host-art" role="img" aria-label="Illustrated portrait of the host in a light blue shirt"></div>
    <svg class="band-panel" viewBox="0 0 364 132" aria-hidden="true">
      <rect width="364" height="132" fill="#0e47a1"/>
      <polygon points="364,10 364,132 150,132" fill="#0a2f78"/>
    </svg>
    <div class="band-title">Broadcast<br>Tinkerings</div>
    <div class="band-credit">A Production of<br>Harbor Fern Audio, LLC</div>
  </section>

  <section class="cover cover--meadow">
    <div class="host-art" role="img" aria-label="Illustrated portrait of the host in a light blue shirt"></div>
    <svg class="meadow-hill" viewBox="0 0 364 174" aria-hidden="true">
      <defs>
        <linearGradient id="meadowFade" x1="0" y1="0" x2="0" y2="1">
          <stop offset="0" stop-color="#6f8f1f"/>
          <stop offset="1" stop-color="#0f1630"/>
        </linearGradient>
      </defs>
      <path d="M0,40 C120,0 250,10 364,30 L364,174 L0,174 Z" fill="url(#meadowFade)" opacity="0.9"/>
      <path d="M0,120 C120,60 250,70 364,110 L364,174 L0,174 Z" fill="#0f1630" opacity="0.85"/>
    </svg>
    <div class="meadow-title">Broadcast Tinkerings</div>
    <div class="meadow-credit">A Production of<br>Harbor Fern Audio, LLC</div>
  </section>

</body>
</html>
```